Creative Businesss Card desgin!

Create a business card for our business Gleam window cleaning!
We are open to creative ideas as long as it maintains a professional image.

Target Market(s)

Small Commercial window cleaning clients including car dealerships, strata manager, cafe

Industry/Entity Type

Window Cleaning

Contact Information for Business Card

Daniel Prescott
General Manager
Gleam Window Cleaning

daniel@gleamservices.com.au
pane-care-southbank.com.au
Ph: 1800 GET GLEAM
Mob: 0437 582 061

Colors
fbed22
0392cd

Requirements
Should not have
• Stock window cleaning/ squeegee graphics

```html
<!DOCTYPE html>
<html lang="en">
<head>
<meta charset="utf-8">
<title>Gleam Window Cleaning — Business Card</title>
<link rel="stylesheet" href="https://fonts.googleapis.com/css2?family=Montserrat:wght@800&family=Quicksand:wght@400&display=swap">
<style>
  :root {
    --backdrop: #232323;
    --navy: #0b5b90;
    --sky: #1697d3;
    --deep: #0a4f80;
    --gleam-yellow: #fbed22;
    --card-w: 700px;
    --card-h: 400px;
  }
  * { box-sizing: border-box; margin: 0; padding: 0; }
  html, body {
    width: 1200px; height: 900px; overflow: hidden;
    background: var(--backdrop);
  }
  .canvas {
    position: relative; width: 1200px; height: 900px;
  }
  .card {
    position: absolute; left: 250px;
    width: var(--card-w); height: var(--card-h);
    overflow: hidden;
    box-shadow: 0 12px 30px rgba(0,0,0,.45);
  }
  .card--front { top: 40px; }
  .card--back  { top: 460px; }
  .card__shapes { position: absolute; inset: 0; width: 100%; height: 100%; }

  .wordmark {
    position: absolute;
    color: var(--gleam-yellow);
    font-family: "Montserrat", sans-serif; font-weight: 800;
    line-height: 1;
  }
  .wordmark__name { display: block; letter-spacing: 2px; }
  .wordmark__tag  { display: block; letter-spacing: 1px; }

  .card--front .wordmark { left: 230px; top: 105px; text-align: center; }
  .card--front .wordmark__name { font-size: 64px; }
  .card--front .wordmark__tag  { font-size: 19px; margin-top: 4px; }

  .card--front .website {
    position: absolute; left: 280px; top: 300px;
    color: var(--gleam-yellow);
    font-family: "Quicksand", sans-serif; font-size: 17px; letter-spacing: .5px;
  }

  .card--back .wordmark { right: 36px; top: 32px; text-align: right; }
  .card--back .wordmark__name { font-size: 44px; }
  .card--back .wordmark__tag  { font-size: 13px; margin-top: 3px; }

  .person { position: absolute; left: 40px; top: 150px; color: var(--gleam-yellow); }
  .person__name {
    font-family: "Montserrat", sans-serif; font-weight: 800; font-size: 28px;
  }
  .person__role {
    font-family: "Quicksand", sans-serif; font-size: 15px; line-height: 1.3;
    margin-top: 4px; padding-bottom: 8px;
    border-bottom: 1px solid var(--gleam-yellow);
    width: 220px;
  }

  .contact-list {
    position: absolute; left: 40px; top: 265px; list-style: none;
    color: var(--gleam-yellow);
    font-family: "Quicksand", sans-serif; font-size: 16px;
  }
  .contact-list__item { display: flex; align-items: center; height: 27px; }
  .contact-list__icon { width: 18px; height: 18px; margin-right: 60px; flex: none; }
</style>
</head>
<body>
<main class="canvas">

  <section class="card card--front" aria-label="Card front">
    <svg class="card__shapes" viewBox="0 0 700 400" preserveAspectRatio="none" aria-hidden="true">
      <rect width="700" height="400" fill="var(--navy)"/>
      <path d="M0 300 C 250 255, 480 185, 700 105 L700 400 L0 400 Z" fill="var(--sky)"/>
      <path d="M330 400 C 470 315, 590 245, 700 190 L700 222 C 600 265, 490 325, 372 400 Z" fill="var(--deep)"/>
    </svg>
    <div class="wordmark">
      <span class="wordmark__name">GLEAM</span>
      <span class="wordmark__tag">WINDOW CLEANING</span>
    </div>
    <p class="website">pane-care-southbank.com.au</p>
  </section>

  <section class="card card--back" aria-label="Card back">
    <svg class="card__shapes" viewBox="0 0 700 400" preserveAspectRatio="none" aria-hidden="true">
      <rect width="700" height="400" fill="var(--sky)"/>
      <path d="M240 0 C 310 115, 500 150, 700 135 L700 0 Z" fill="var(--navy)"/>
      <path d="M390 400 C 490 320, 610 270, 700 245 L700 400 Z" fill="var(--deep)"/>
    </svg>
    <div class="wordmark">
      <span class="wordmark__name">GLEAM</span>
      <span class="wordmark__tag">WINDOW CLEANING</span>
    </div>

    <div class="person">
      <h1 class="person__name">Daniel Prescott</h1>
      <p class="person__role">General Manager<br>Gleam Window Cleaning</p>
    </div>

    <ul class="contact-list">
      <li class="contact-list__item">
        <svg class="contact-list__icon" viewBox="0 0 24 24" aria-hidden="true"><path fill="var(--gleam-yellow)" d="M3 9c0-3 4-5 9-5s9 2 9 5l-4 1-1-3H8L7 10 3 9zm4 2h10l3 7v2H4v-2l3-7zm5 2a2.5 2.5 0 1 0 0 5 2.5 2.5 0 0 0 0-5z"/></svg>
        1800 GET GLEAM
      </li>
      <li class="contact-list__item">
        <svg class="contact-list__icon" viewBox="0 0 24 24" aria-hidden="true"><rect x="6" y="2" width="12" height="20" rx="2" fill="none" stroke="var(--gleam-yellow)" stroke-width="2"/></svg>
        0437 582 061
      </li>
      <li class="contact-list__item">
        <svg class="contact-list__icon" viewBox="0 0 24 24" aria-hidden="true"><rect x="2" y="5" width="20" height="14" fill="var(--gleam-yellow)"/><path d="M2 5l10 8 10-8" fill="none" stroke="var(--sky)" stroke-width="1.5"/></svg>
        daniel@gleamservices.com.au
      </li>
      <li class="contact-list__item">
        <svg class="contact-list__icon" viewBox="0 0 24 24" aria-hidden="true"><g fill="none" stroke="var(--gleam-yellow)" stroke-width="2"><circle cx="12" cy="12" r="9"/><ellipse cx="12" cy="12" rx="4" ry="9"/><path d="M3 12h18M5 7h14M5 17h14"/></g></svg>
        pane-care-southbank.com.au
      </li>
    </ul>
  </section>

</main>
</body>
</html>
```